flatrotate.co.uk landing page website design

Hi designers, I would like a custom designed landing page very similar to www.dwellingtrader.co.uk. It represents a happy place, sunny days and people swapping homes. I would like this done just like theres but our own design but a similar layout as theres.

I would like the 3 reasons to use us to be

Connect to thousands of other people in your area looking for a home swap

Our service is Completely free unlike most other exchange websites.

Find a exchange within 30 days!*

Thank you all,

Hi Everyone, I need the designs to represent london if possible like one of the designers has done for anyone else being in with a chance to win. Please check out the design by KR with the london look. I still like some of the others and they may win but i need to give this a try please.

Target Market(s)

Council house tenants

Coding

Coded - Design and coding required

Number of Pages Required

1 page

Requirements
Must have
• Custom designed landing page showing all the elements that www.dwellingtrader.co.uk use, The blue sky, and the land it shows with houses and people representing people swapping house. It can not be the same as them but can be similar concept with our own custom design and colour scheme ect.

please create 3 bubbles for speech from people. Please add the following quotes. "Its time we upsize"
"lets try and downsize and save money" "shall we move house?"
Would like 2 blocks of flats in a similar way dwelling trader.co.uk show the houses.
Nice to have

Should not have
• Same colour scheme as dwelling trader apart from the blue sky

```html
<!DOCTYPE html>
<html lang="en">
<head>
<meta charset="utf-8">
<title>FlatRotate – Your Dream Home is a Moment Away</title>
<link href="https://fonts.googleapis.com/css2?family=Hind:wght@300;400;500;600&display=swap" rel="stylesheet">
<style>
:root{
  --sky:#86cde9;
  --sky-light:#bfe2f5;
  --panel:#5aabd0;
  --gold:#d9c86c;
  --ink:#2f3a44;
  --ink-soft:#44515c;
  --road:#75787f;
  --foot-bar:#9b9b9b;
  --white:#ffffff;
  --cloud-grey:#c5d3e0;
  --grass:#9ee88a;
}
*{box-sizing:border-box;margin:0;padding:0}
html,body{width:1200px;height:3105px;overflow:hidden}
body{position:relative;font-family:'Hind',sans-serif;color:var(--ink);background:var(--sky)}
.abs{position:absolute}

/* hero */
.hero{left:0;top:0;width:1200px;height:1132px;background:var(--sky)}
.sky-top{left:0;top:0;width:1200px;height:275px;
  background:linear-gradient(180deg,#ffffff 0%,#f1f3f6 40%,var(--cloud-grey) 78%,var(--sky) 100%)}
.brand-title{left:0;top:292px;width:1200px;text-align:center;font-size:41px;font-weight:500;color:var(--ink)}
.brand-tag{left:0;top:344px;width:1200px;text-align:center;font-size:19px;font-weight:400;color:var(--ink-soft)}

.search{left:189px;top:452px;width:825px;height:149px;background:var(--panel);border-radius:10px}
.search-label{top:36px;font-size:21px;font-weight:500;color:var(--ink)}
.field{top:71px;width:195px;height:37px;background:var(--white);border-radius:8px;font-size:13px;color:#8a8f96;padding:11px 15px}
.field svg{position:absolute;right:14px;top:15px}
.btn{background:var(--gold);color:#3b3a2a;border-radius:12px;font-size:13px;text-align:center;font-weight:400}
.search .btn{left:653px;top:71px;width:150px;height:37px;line-height:39px}

.reason{top:656px;font-size:18px;line-height:36px;color:var(--ink);padding-left:41px}
.reason svg{position:absolute;left:0;top:2px}

.sky-bottom{left:0;top:783px;width:1200px;height:349px;
  background:linear-gradient(180deg,var(--sky) 0%,#b8e0f4 35%,#eef6fb 70%,#ffffff 100%)}

/* about */
.about{left:0;top:1132px;width:1200px;height:1040px;background:var(--sky-light)}
.about-title{left:0;top:1185px;width:1200px;text-align:center;font-size:28px;font-weight:400;color:var(--ink)}
.about-text{left:185px;top:1231px;width:830px;text-align:center;font-size:21.5px;line-height:31.5px;font-weight:300;color:var(--ink-soft)}
.about-btn{left:523px;top:1348px;width:150px;height:37px;line-height:39px}
.rule{left:149px;width:900px;height:1px}
.rule-blue{top:1442px;background:#a9cfe6}
.how-title{left:0;top:1497px;width:1200px;text-align:center;font-size:27px;font-weight:400;color:var(--ink)}
.step{top:1559px;width:260px;text-align:center}
.step-icon{width:116px;height:116px;margin:0 auto;border:2px solid var(--gold);border-radius:50%;display:flex;align-items:center;justify-content:center;box-shadow:0 3px 5px rgba(0,0,0,.08)}
.step-name{margin-top:22px;font-size:17px;font-weight:500;color:var(--ink)}
.step-text{margin:6px auto 0;width:250px;font-size:13.5px;line-height:20.3px;font-weight:300;color:var(--ink-soft)}

/* street scene */
.street{left:0;top:1915px;width:1200px;height:240px;
  background:
    linear-gradient(180deg,rgba(191,226,245,0) 0%,rgba(191,226,245,0) 88%,var(--grass) 88%,var(--grass) 100%),
    linear-gradient(90deg,#b9d48a 0%,#7cc492 16%,#d7e9e6 24%,#6fc45a 30%,#efc4bd 44%,#a9a6e0 57%,#d7e9e6 66%,#6fc45a 71%,#e8c4ea 84%,#e9efbf 95%,#6fc45a 100%)}
.bubble{background:var(--white);border-radius:50%;display:flex;align-items:center;justify-content:center;text-align:center;font-size:12px;line-height:17px;color:#333}
.bubble::after{content:"";position:absolute;bottom:-10px;left:50%;border:8px solid transparent;border-top:12px solid var(--white)}

/* contact */
.contact{left:0;top:2155px;width:1200px;height:913px;background:var(--road)}
.lane{left:0;top:2168px;width:1200px;height:3px;background:repeating-linear-gradient(90deg,#ffffff 0 30px,transparent 30px 57px)}
.contact-title{left:149px;top:2241px;font-size:27px;font-weight:400;color:var(--white)}
.input{height:37px;background:var(--white);border-radius:10px;font-size:13px;color:#8a8f96;padding:11px 15px}
.message{left:150px;top:2425px;width:899px;height:226px}
.submit{left:150px;top:2673px;width:150px;height:37px;line-height:39px}
.rule-light{top:2763px;background:#d6d7da}
.foot-brand{left:149px;top:2826px;font-size:32px;font-weight:400;color:var(--white)}
.foot-head{top:2832px;font-size:17px;font-weight:500;color:var(--white)}
.foot-text{font-size:12.8px;line-height:20.3px;font-weight:400;color:var(--white)}
.hours span{display:inline-block;width:35px}
.copyright{left:0;top:3068px;width:1200px;height:37px;background:var(--foot-bar);color:var(--white);text-align:center;font-size:13px;line-height:39px}
</style>
</head>
<body>

<section class="abs hero">
  <div class="abs sky-top" role="img" aria-label="Illustration of a bright sun behind a bank of white and grey clouds"></div>
  <h1 class="abs brand-title">FlatRotate</h1>
  <p class="abs brand-tag">Your Dream Home is a Moment Away.</p>

  <form class="abs search">
    <span class="abs search-label" style="left:28px">Location</span>
    <span class="abs search-label" style="left:238px">Bedrooms</span>
    <span class="abs search-label" style="left:448px">Max. Rent/Mo</span>
    <div class="abs field" style="left:23px">Town</div>
    <div class="abs field" style="left:233px">Any<svg width="12" height="7" viewBox="0 0 12 7"><path d="M1 1l5 5 5-5" fill="none" stroke="#9aa0a6" stroke-width="1.3"/></svg></div>
    <div class="abs field" style="left:443px">Any<svg width="12" height="7" viewBox="0 0 12 7"><path d="M1 1l5 5 5-5" fill="none" stroke="#9aa0a6" stroke-width="1.3"/></svg></div>
    <div class="abs btn">Find me a home</div>
  </form>

  <div class="abs reason" style="left:187px;width:290px">
    <svg width="32" height="30" viewBox="0 0 32 30"><path d="M2 16c6-1 10 1 13 4 2-6 6-12 14-17-3 6-4 11-6 15 3 0 6-1 8-2-3 4-7 7-12 7l-3 6-2-5c-5 0-9-3-12-8z" fill="#ffffff"/></svg>
    Connect to thousands of other people in your area looking for a home swap
  </div>
  <div class="abs reason" style="left:483px;width:290px">
    <svg width="32" height="30" viewBox="0 0 32 30"><path d="M2 16c6-1 10 1 13 4 2-6 6-12 14-17-3 6-4 11-6 15 3 0 6-1 8-2-3 4-7 7-12 7l-3 6-2-5c-5 0-9-3-12-8z" fill="#ffffff"/></svg>
    Our service is Completely free unlike most other exchange websites.
  </div>
  <div class="abs reason" style="left:774px;width:260px">
    <svg width="32" height="30" viewBox="0 0 32 30"><path d="M2 16c6-1 10 1 13 4 2-6 6-12 14-17-3 6-4 11-6 15 3 0 6-1 8-2-3 4-7 7-12 7l-3 6-2-5c-5 0-9-3-12-8z" fill="#ffffff"/></svg>
    Find a exchange within 30 days!*
  </div>

  <div class="abs sky-bottom" role="img" aria-label="Illustrated bank of fluffy white clouds"></div>
</section>

<section class="abs about"></section>
<h2 class="abs about-title">We are changing the way people exchange council homes</h2>
<p class="abs about-text">It can be a difficult and time consuming process finding your next property exchange. Our free service is proven to find your home swap faster with very little stress. We connect you to hundreds of thousands of other people look.</p>
<div class="abs btn about-btn">Contact us</div>
<div class="abs rule rule-blue"></div>

<h2 class="abs how-title">How Does It Work?</h2>
<div class="abs step" style="left:166px">
  <div class="step-icon"><svg width="54" height="48" viewBox="0 0 54 48" fill="none" stroke="#5b6670" stroke-width="1.6"><rect x="20" y="4" width="30" height="22" rx="2"/><path d="M20 6l15 11 15-11"/><path d="M8 14c-4 3-4 10 2 18s14 12 19 10l3-4-7-5-3 3c-4-2-8-7-9-11l3-3-4-7z"/></svg></div>
  <div class="step-name">Step 1</div>
  <p class="step-text">Call us or leave us your details. We need to know some details about your property and your requirements for the next one your looking for so we can move on to step 2.</p>
</div>
<div class="abs step" style="left:469px">
  <div class="step-icon"><svg width="56" height="48" viewBox="0 0 56 48" fill="none" stroke="#5b6670" stroke-width="1.6"><rect x="6" y="4" width="44" height="34" rx="2"/><path d="M6 11h44"/><circle cx="42" cy="22" r="6"/><path d="M14 20h8l10-6v20l-10-6h-8z"/><path d="M17 28l3 12h5l-2-12"/></svg></div>
  <div class="step-name">Step 2</div>
  <p class="step-text">We will know advertise your property on over 50 online and offline platforms to ensure you find a suitable match as quickly as possible.</p>
</div>
<div class="abs step" style="left:772px">
  <div class="step-icon"><svg width="54" height="48" viewBox="0 0 54 48" fill="none" stroke="#5b6670" stroke-width="1.6"><path d="M4 22L27 4l23 18"/><path d="M10 18v26h34V18"/><circle cx="27" cy="18" r="4"/><rect x="15" y="28" width="9" height="16"/><rect x="29" y="28" width="11" height="9"/><path d="M34.5 28v9M29 32.5h11"/></svg></div>
  <div class="step-name">Step 3</div>
  <p class="step-text">We find your new dream home for you by matching you to as many suitable properties as possible as well as ensuring we save you money where possible too.</p>
</div>

<div class="abs street" role="img" aria-label="Illustrated street of pastel terraced houses and blocks of flats with trees, bicycles and benches"></div>
<div class="abs bubble" style="left:245px;top:1900px;width:130px;height:64px">Its time we upsize</div>
<div class="abs bubble" style="left:713px;top:1900px;width:130px;height:68px">Lets try and downsize<br>and save money</div>
<div class="abs bubble" style="left:1052px;top:1902px;width:130px;height:64px">Shall we move house?</div>

<section class="abs contact"></section>
<div class="abs lane"></div>
<h2 class="abs contact-title">Contact Us</h2>
<div class="abs input" style="left:150px;top:2305px;width:242px">Name *</div>
<div class="abs input" style="left:413px;top:2305px;width:242px">Phone number *</div>
<div class="abs input" style="left:676px;top:2305px;width:373px">Email *</div>
<div class="abs input" style="left:150px;top:2365px;width:242px">Address *</div>
<div class="abs input" style="left:413px;top:2365px;width:242px">Post code *</div>
<div class="abs input" style="left:676px;top:2365px;width:175px">House/Flat *</div>
<div class="abs input" style="left:873px;top:2365px;width:176px">Number of bedrooms *</div>
<div class="abs input message">Message *</div>
<div class="abs btn submit">Submit</div>
<div class="abs rule rule-light"></div>

<footer>
  <div class="abs foot-brand">FlatRotate</div>
  <p class="abs foot-text" style="left:158px;top:2877px;width:275px">We are always happy to hear from you Call us today to see how we can help you.<br>020 7946 0321</p>
  <p class="abs foot-text" style="left:158px;top:2958px;width:290px">* Guaranteed 30 day house exchange subject to using our partner company reduced rent for their services.</p>

  <h3 class="abs foot-head" style="left:543px">Working hours</h3>
  <p class="abs foot-text hours" style="left:543px;top:2877px;width:200px">
    <span>Mon:</span>08:00 – 20:00<br>
    <span>Tue:</span>08:00 – 20:00<br>
    <span>Wed:</span>08:00 – 20:00<br>
    <span>Thu :</span>08:00 – 20:00<br>
    <span>Fri:</span>08:00 – 20:00<br>
    <span>Sat:</span>08:00 – 20:00<br>
    <span>Sun:</span>Closed
  </p>

  <h3 class="abs foot-head" style="left:813px">Contact Us</h3>
  <p class="abs foot-text" style="left:813px;top:2877px;width:240px">020 7946 0321<br>Info@flatrotate.co.uk</p>

  <div class="abs copyright">Copyright © 2020 Flatrotate - All Rights Reserved.</div>
</footer>

</body>
</html>
```